Graphic Design for Labels

I'm needing a label for my skincare line based in Alder Bay, NS. The name of the company is 'Velvet Dawn Skincare' and the tag line is 'Stay Kind to Your Face'. It should indicate somewhere on the lable that it is made with raw fireweed honey.
There are two products the first is Moisturizing Face Cream and second is Nourishing Face Buff. I would like some honey-comb incorporated around the edges of the label and a black and white detailed honeybee somewhere on the label, maybe looking like it was hand drawn with a fine tip black marker or pencil. It will need to have the amount of product in the front which is 120 ml.
I'm open to different colours but nothing too bright, I want a delicate feel to the colours. Overall I would like the label to have a boutiquey artisan feel. I will also require an ingredient label for the back of the bottles the exact same size as the front label with the company info there as well. And some directions. The ingredients and directions can read whatever for now and I will provide those details when I'm ready to order the labels if that's possible, if not let me know asap and I can provide the details. After the ingredients list I would like it to read:
'Paraben and Sulfate free'
At the bottom of the back label I would like it to read:
'Please Recycle'
and then the company name and location at the very bottom
Updates
I like the way this label is organized, and especially how the company name is in the circle around the butterfly. Maybe that could be done with a honey bee and if the Net Weight could be included like it is on this bottle that would be great - 4 oz (115g)
The flowers are nice, but maybe it would look good to have simlpe hand drawn flowers with a bee flying around, if possible?

```html
<!DOCTYPE html>
<html lang="en">
<head>
<meta charset="utf-8">
<title>Velvet Dawn Skincare – Moisturizing Face Cream Labels</title>
<link rel="stylesheet" href="https://fonts.googleapis.com/css2?family=Josefin+Sans:wght@300;400&family=Raleway:wght@300;400&family=Caveat:wght@500&display=swap">
<style>
  :root {
    --page: #ffffff;
    --label: #f3f4f5;
    --honey: #f5b82e;
    --honey-soft: #fbe3a6;
    --ink: #4a4a4c;
    --ink-soft: #7a7b7d;
    --line-grey: #c9cacc;
  }
  * { margin: 0; padding: 0; box-sizing: border-box; }
  html, body { width: 1200px; height: 1000px; overflow: hidden; background: var(--page); }
  .canvas { position: relative; width: 1200px; height: 1000px; }

  .label {
    position: absolute;
    top: 100px;
    width: 290px;
    height: 650px;
    background: var(--label);
    border-radius: 6px;
    font-family: "Raleway", sans-serif;
    color: var(--ink);
  }
  .label--front { left: 185px; }
  .label--back { left: 715px; }

  .comb-field {
    position: absolute;
    border-radius: 50%;
    background: radial-gradient(circle, rgba(245,184,46,0.18) 0%, rgba(245,184,46,0) 70%);
  }

  .brand { position: absolute; left: 0; width: 100%; text-align: center; }
  .brand__dot {
    display: block; margin: 0 auto 14px;
    width: 58px; height: 58px; border-radius: 50%;
    background: var(--honey);
  }
  .brand__name {
    font-family: "Josefin Sans", sans-serif; font-weight: 300;
    color: var(--ink); font-size: 22px; letter-spacing: 1px; line-height: 1.1;
    text-transform: uppercase;
  }
  .brand__name small {
    display: block; font-size: 13px; letter-spacing: 3px; text-transform: lowercase; margin-top: 4px;
  }
  .label--front .brand { top: 100px; }

  .product-name {
    position: absolute; left: 168px; top: 262px;
    writing-mode: vertical-rl;
    font-family: "Josefin Sans", sans-serif; font-weight: 300;
    font-size: 19px; letter-spacing: 0; line-height: 1; color: var(--ink);
    white-space: nowrap;
  }
  .tagline {
    position: absolute; left: 132px; top: 310px;
    writing-mode: vertical-rl;
    font-family: "Caveat", cursive; font-size: 18px; line-height: 1; color: var(--honey); letter-spacing: 1px;
    white-space: nowrap;
  }
  .tagline-rule {
    position: absolute; left: 125px; top: 322px; width: 2px; height: 140px;
    background: var(--honey); border-radius: 2px;
  }
  .net-weight {
    position: absolute; left: 0; width: 100%; top: 562px; text-align: center;
    font-size: 12px; color: var(--ink);
  }

  .flower-band {
    position: absolute; left: 0; bottom: 0; width: 100%; height: 70px;
    background: linear-gradient(180deg, rgba(243,244,245,0) 0%, var(--honey-soft) 45%, #e3e3e5 100%);
    border-radius: 0 0 6px 6px;
  }

  .section-title {
    font-family: "Josefin Sans", sans-serif; font-weight: 400;
    font-size: 10px; color: var(--honey); letter-spacing: 0.5px; text-transform: uppercase;
    margin-bottom: 4px;
  }
  .ingredients { position: absolute; left: 24px; right: 24px; top: 90px; }
  .ingredients p { font-size: 7.5px; line-height: 1.25; text-align: justify; color: var(--ink-soft); }
  .free-from { position: absolute; left: 0; width: 100%; top: 184px; text-align: center; font-size: 8.5px; }

  .directions { position: absolute; left: 30px; right: 24px; top: 222px; }
  .steps { list-style: none; }
  .step { display: flex; align-items: flex-start; gap: 8px; margin-bottom: 8px; }
  .step__num {
    flex: 0 0 24px; height: 22px;
    clip-path: polygon(25% 0, 75% 0, 100% 50%, 75% 100%, 25% 100%, 0 50%);
    background: var(--honey); color: #fff;
    font-size: 11px; display: flex; align-items: center; justify-content: center; margin-top: 2px;
  }
  .step p { font-size: 7.5px; line-height: 1.2; color: var(--ink-soft); }
  .recycle {
    position: absolute; left: 0; width: 100%; top: 353px; text-align: center;
    font-size: 8.5px; text-transform: uppercase; letter-spacing: 0.3px;
  }
  .label--back .brand { top: 438px; }
  .label--back .brand__dot { width: 50px; height: 50px; margin-bottom: 10px; }
  .label--back .brand__name { font-size: 18px; }
  .label--back .brand__name small { font-size: 11px; }
  .location { position: absolute; left: 0; width: 100%; top: 544px; text-align: center; font-size: 7px; color: var(--ink-soft); }
</style>
</head>
<body>
<main class="canvas">

  <section class="label label--front" aria-label="Front label">
    <div class="comb-field" role="img" aria-label="Scattered honeycomb outlines" style="left:20px;top:70px;width:90px;height:180px;"></div>
    <div class="comb-field" role="img" aria-label="Scattered honeycomb outlines" style="left:200px;top:70px;width:90px;height:200px;"></div>

    <div class="brand">
      <span class="brand__dot"></span>
      <p class="brand__name">Velvet Dawn<small>skincare</small></p>
    </div>

    <span class="tagline-rule"></span>
    <p class="tagline">Stay Kind to Your Face</p>
    <h1 class="product-name">MOISTURIZING FACE CREAM</h1>

    <p class="net-weight">115 g</p>

    <div class="flower-band" role="img" aria-label="Hand-drawn wildflowers and dandelions in honey yellow and grey"></div>
  </section>

  <section class="label label--back" aria-label="Back label">
    <div class="ingredients">
      <h2 class="section-title">Ingredients</h2>
      <p>Aqua, raw fireweed honey, sunflower seed oil, shea butter, glycerin, oat kernel extract, beeswax, jojoba seed oil, aloe leaf juice, cetearyl alcohol, vitamin E, chamomile flower extract, calendula extract, rosehip oil, xanthan gum, lavender oil, citric acid, sodium benzoate, potassium sorbate and a touch of natural fragrance from wildflowers.</p>
    </div>
    <p class="free-from">Paraben and Sulfate Free</p>

    <div class="directions">
      <h2 class="section-title">Direction</h2>
      <ol class="steps">
        <li class="step"><span class="step__num">1</span><p>Cleanse your face with warm water and gently pat the skin dry with a soft towel before applying.</p></li>
        <li class="step"><span class="step__num">2</span><p>Warm a small amount between your fingertips and smooth it over face and neck in slow upward circles.</p></li>
        <li class="step"><span class="step__num">3</span><p>Use morning and night. Store in a cool dry place away from direct sunlight.</p></li>
      </ol>
    </div>

    <p class="recycle">Please Recycle</p>

    <div class="comb-field" role="img" aria-label="Scattered honeycomb outlines" style="left:10px;top:415px;width:90px;height:160px;"></div>
    <div class="comb-field" role="img" aria-label="Scattered honeycomb outlines" style="left:190px;top:415px;width:90px;height:160px;"></div>

    <div class="brand">
      <span class="brand__dot"></span>
      <p class="brand__name">Velvet Dawn<small>skincare</small></p>
    </div>
    <p class="location">Alder Bay, NS</p>

    <div class="flower-band" role="img" aria-label="Hand-drawn wildflowers and dandelions in honey yellow and grey"></div>
  </section>

</main>
</body>
</html>
```